Brightmeadow Charity Ball Poster

We are looking for a poster for our upcoming event, "Brightmeadow Charity Ball" - a sit down dinner formal event hosted by our university club, OKRU.
Usually we source designs internally from our committee (even if they aren't the most amazing quality), however this time round we have no one available to do it as everyone is a volunteer.
The event's theme is 'winter wonderland', based around the snowy forests you see in Velmoria or Crown of Ashes (neither of these specific things are the theme however). Our venue is a clear-roof marque in a space surrounded by very tall pine trees giving off the forest vibe, and there are festoons strung between the trees so this is an element of warm light amongst the forest, perhaps a building or village tucked away in the forest.
The poster is for printing out at A3 size, and we will also need to create a Chatterbook event cover photo and other marketing graphics from the original poster files so some flexibility in the design and original files are required.
Things that need to be included on the poster :
---Event details
Brightmeadow Charity Ball
Saturday 12th August
7pm – midnight
Harrowgate Auditorium, KPT
Tables of 10
Members - $140
Non members - $150
All profits donated to Stride for Hope
---- Extra info and images (can be at the bottom, in corners etc,)
18+ ID required | Drink Responsibly
OKRU Logo
KPT Guild Logo
(these logos may be changed to black and white if need be)
Example images of styles, colours and the sort of landscape we want for the poster can be found in the document attached.

```html
<!DOCTYPE html>
<html lang="en">
<head>
<meta charset="utf-8">
<title>Brightmeadow Charity Ball</title>
<link href="https://fonts.googleapis.com/css2?family=Great+Vibes&family=Raleway:wght@300;400;600;700&display=swap" rel="stylesheet">
<style>
  :root{
    --ink:#1e1a1c;
    --maroon:#74203e;
    --white:#ffffff;
    --rule:#9a5a72;
    --forest-dark:#2a1420;
    --forest-ember:#a8401f;
    --glow:#fff6ec;
  }
  *{margin:0;padding:0;box-sizing:border-box}
  html,body{width:849px;height:1200px;overflow:hidden;background:var(--white)}
  .poster{position:relative;width:849px;height:1200px;overflow:hidden;font-family:"Raleway",sans-serif;color:var(--ink)}
  .forest-scene{position:absolute;inset:0;
    background:
      radial-gradient(ellipse 300px 380px at 400px 560px, rgba(255,255,255,1) 0%, rgba(255,250,240,.9) 35%, rgba(255,240,230,0) 75%),
      radial-gradient(ellipse 260px 220px at 360px 330px, rgba(150,40,60,.75) 0%, rgba(120,30,50,0) 80%),
      linear-gradient(90deg, rgba(120,40,20,.55) 0%, rgba(0,0,0,0) 30%, rgba(0,0,0,0) 70%, rgba(160,110,50,.45) 100%),
      linear-gradient(180deg, var(--forest-dark) 0%, #5a2222 14%, var(--forest-ember) 30%, #d9a9a0 48%, var(--glow) 66%, #ffffff 100%);}
  .footer-fade{position:absolute;left:0;right:0;bottom:0;height:200px;background:linear-gradient(180deg,rgba(255,255,255,0),#fff 45%)}
  .club-mark{position:absolute;left:0;right:0;top:98px;display:flex;justify-content:center;align-items:center;gap:10px}
  .club-mark .dot{width:22px;height:22px;border-radius:50%;background:var(--maroon)}
  .club-mark .name{font-size:40px;font-weight:700;color:var(--white);letter-spacing:2px}
  .centered{position:absolute;left:0;right:0;text-align:center}
  .presents{top:245px;font-size:24px;font-weight:400;color:var(--white);letter-spacing:1px}
  .event-title{top:258px;font-family:"Great Vibes",cursive;font-size:118px;line-height:1;font-weight:400;color:var(--white);text-shadow:0 3px 6px rgba(0,0,0,.35)}
  .event-subtitle{top:386px;font-size:38px;font-weight:300;color:var(--white);letter-spacing:1px}
  .details{top:662px;font-size:22px;line-height:29px;font-weight:400}
  .pricing{top:780px;font-size:22px;line-height:30px}
  .pricing .label{color:var(--maroon);font-weight:700}
  .proceeds{top:895px;font-size:27px;line-height:35px;font-weight:700;color:var(--maroon)}
  .notice{top:996px;font-size:16px}
  .sponsor-labels{position:absolute;top:1082px;left:46px;right:37px;height:20px}
  .sponsor-labels .tag{position:absolute;top:0;font-size:17px;color:var(--maroon);letter-spacing:.5px}
  .sponsor-labels .rule{position:absolute;top:10px;height:1px;background:var(--rule)}
  .logo-row{position:absolute;top:1122px;height:56px;left:0;right:0}
  .sponsor{position:absolute;top:0;width:96px;margin-left:-48px;height:56px;display:flex;flex-direction:column;align-items:center;justify-content:center;gap:4px;text-align:center;font-size:11px;font-weight:600;color:var(--ink);line-height:1.2;white-space:nowrap}
  .sponsor .sq{width:12px;height:12px;background:var(--maroon);flex:none}
  .sponsor .ci{width:12px;height:12px;border-radius:50%;background:var(--ink);flex:none}
</style>
</head>
<body>
<div class="poster">
  <div class="forest-scene" role="img" aria-label="Night forest of tall snowy pine trees lit with warm festoon lights and a bright glow between the trunks"></div>
  <div class="footer-fade"></div>

  <div class="club-mark"><span class="dot"></span><span class="name">OKRU</span></div>

  <p class="centered presents">PRESENTS THE</p>
  <h1 class="centered event-title">Brightmeadow</h1>
  <p class="centered event-subtitle">CHARITY BALL</p>

  <p class="centered details">Saturday, August 12th<br>7pm - Midnight<br>Harrowgate Auditorium, KPT</p>
  <p class="centered pricing"><span class="label">Tables of 10</span><br>Members - $140<br>Non Members - $150</p>
  <p class="centered proceeds">ALL PROCEEDS TO<br>STRIDE FOR HOPE KPT</p>
  <p class="centered notice">18+ ID Required | Drink Responsibly</p>

  <div class="sponsor-labels">
    <span class="tag" style="left:0">MAJOR PARTNER</span>
    <span class="rule" style="left:194px;width:190px"></span>
    <span class="tag" style="left:403px">EVENT SPONSORS</span>
    <span class="rule" style="left:570px;width:242px"></span>
  </div>

  <div class="logo-row">
    <div class="sponsor" style="left:118px"><span class="sq"></span><span>Larkfield<br>Event Hire</span></div>
    <div class="sponsor" style="left:298px"><span class="ci"></span><span>Vane<br>Photo &amp; Film</span></div>
    <div class="sponsor" style="left:418px"><span>Dorian Halsey<br>Photographer</span></div>
    <div class="sponsor" style="left:566px"><span class="ci"></span><span>Keystone<br>Security</span></div>
    <div class="sponsor" style="left:669px"><span>Copper Kettle<br>Roast</span></div>
    <div class="sponsor" style="left:748px"><span class="sq"></span><span>KPT<br>Guild</span></div>
  </div>
</div>
</body>
</html>
```